Design a Website Mockup for a Job Search Engine

This design contest is for a Job Search Engine.
Similar to popular job search engines like: [login to view URL], [login to view URL], [login to view URL] and [login to view URL]
I require a modern beautiful design that is not too overpowering but blows the above sites away.
The design must be highly driven toward the perfect user experience with guidance on the correct fonts to be used and search result placement for best visibility.
The pages that i require mocked up:
Homepage, Search Results (check out [login to view URL] or [login to view URL] for the type of data that will be shown on the results page), About page
Please be creative as possible.
The winner will be the mockup that displays the best UX experience with a modern catchy design.
Please note the site will be a responsive design so please also show mockups for tablet and mobile as well as desktop for all above pages.

```html
<!DOCTYPE html>
<html lang="en">
<head>
<meta charset="utf-8">
<title>JobHarbor – Find Jobs</title>
<link rel="stylesheet" href="https://fonts.googleapis.com/css2?family=Cabin:wght@400;500;600&family=Oswald:wght@500&family=Arimo:wght@400;700&display=swap">
<style>
  :root {
    --sky-light: #2a6f8f;
    --sky-mid: #1b5473;
    --sky-dark: #0d2c42;
    --ink: #000000;
    --white: #ffffff;
    --panel: rgba(255, 255, 255, 0.16);
    --button: #163d59;
    --label: #0f2233;
    --placeholder: #8a8a8a;
  }
  * { box-sizing: border-box; margin: 0; padding: 0; }
  html, body { width: 1200px; height: 612px; overflow: hidden; }
  body { font-family: "Cabin", sans-serif; color: var(--white); position: relative; background: var(--sky-dark); }

  .hero-backdrop {
    position: absolute; inset: 0;
    background:
      radial-gradient(ellipse 60% 70% at 50% 45%, var(--sky-light) 0%, transparent 75%),
      linear-gradient(180deg, var(--sky-mid) 0%, var(--sky-dark) 100%);
  }
  .top-rule { position: absolute; top: 0; left: 0; right: 0; height: 4px; background: var(--ink); }

  .site-header { position: absolute; top: 0; left: 0; right: 0; height: 52px; }
  .brand {
    position: absolute; left: 53px; top: 14px;
    display: flex; align-items: center; gap: 8px;
    font-weight: 600; font-size: 15px; letter-spacing: 0.5px;
  }
  .brand-mark { width: 20px; height: 20px; background: var(--white); }
  .main-nav { position: absolute; top: 17px; left: 179px; display: flex; gap: 46px; font-size: 14px; font-weight: 500; }
  .main-nav a { color: var(--white); text-decoration: none; }

  .account-links {
    position: absolute; left: 867px; top: 0; width: 144px; height: 25px;
    background: var(--ink); border-radius: 0 0 6px 6px;
    display: flex; align-items: center; justify-content: center; gap: 16px;
    font-family: "Arimo", sans-serif; font-size: 12px;
  }
  .account-links a { color: var(--white); text-decoration: none; display: flex; align-items: center; gap: 4px; }

  .hero-copy { position: absolute; top: 185px; left: 0; right: 0; text-align: center; }
  .hero-title { font-size: 30px; font-weight: 600; letter-spacing: 0.2px; }
  .hero-lead { margin: 10px auto 0; width: 460px; font-size: 17px; line-height: 22px; }

  .job-search {
    position: absolute; left: 275px; top: 287px; width: 642px; height: 78px;
    background: var(--panel);
  }
  .field { position: absolute; top: 9px; }
  .field-label { display: block; font-family: "Arimo", sans-serif; font-size: 9px; font-weight: 700; color: var(--label); margin-bottom: 4px; }
  .field input {
    height: 29px; border: none; background: var(--white);
    font-family: "Arimo", sans-serif; font-size: 9px; padding: 0 6px; color: #333;
  }
  .field input::placeholder { color: var(--placeholder); }
  .field-what { left: 22px; }
  .field-what input { width: 202px; }
  .field-where { left: 260px; }
  .field-where input { width: 209px; }
  .search-button {
    position: absolute; left: 489px; top: 25px; width: 129px; height: 28px;
    background: var(--button); color: var(--white); border: none;
    font-family: "Oswald", sans-serif; font-size: 15px; letter-spacing: 0.3px;
  }

  .site-footer {
    position: absolute; left: 0; right: 0; bottom: 0; height: 24px; background: var(--ink);
    display: flex; align-items: center; justify-content: center;
    font-family: "Arimo", sans-serif; font-size: 8px; color: var(--white);
  }
</style>
</head>
<body>
  <div class="hero-backdrop" role="img" aria-label="Blue-tinted photograph of city skyscrapers"></div>
  <div class="top-rule"></div>

  <header class="site-header">
    <div class="brand"><span class="brand-mark"></span>JobHarbor</div>
    <nav class="main-nav">
      <a href="#">Find Jobs</a>
      <a href="#">Employers</a>
      <a href="#">Post Job (free)</a>
      <a href="#">Post Your CV</a>
    </nav>
    <div class="account-links">
      <a href="#">
        <svg width="11" height="11" viewBox="0 0 12 12" fill="none" stroke="#fff" stroke-width="1.5"><path d="M1 6h7M5.5 3.5 8 6 5.5 8.5M8 1.5h2.5v9H8"/></svg>Login
      </a>
      <a href="#">
        <svg width="10" height="11" viewBox="0 0 10 11" fill="#fff"><circle cx="5" cy="3" r="2.5"/><path d="M0 11c0-3 2.2-4.5 5-4.5S10 8 10 11z"/></svg>Sign Up
      </a>
    </div>
  </header>

  <section class="hero-copy">
    <h1 class="hero-title">Discover millions of jobs related to your skills</h1>
    <p class="hero-lead">The right job close to your home or across the country. we make it easy for you to find the right job</p>
  </section>

  <form class="job-search">
    <label class="field field-what">
      <span class="field-label">What do you want to do?</span>
      <input type="text" placeholder="Job title, skills or company">
    </label>
    <label class="field field-where">
      <span class="field-label">What do you want to do?</span>
      <input type="text" placeholder="City, State or Zip">
    </label>
    <button class="search-button" type="button">SEARCH NOW</button>
  </form>

  <footer class="site-footer">© jobharborsite.com · All rights reserved · Contact Us · Privacy Policy</footer>
</body>
</html>
```